New Wine Label - Argentinian Malbec 'Viento Callado'

I am looking for an exceptional and exciting design for a wine label called 'Viento Callado' meaning Quiet Wind or Wind of the Quiet. The design must feature the name 'Viento Callado', a star logo and the word 'Malbec'. It will also need the words 'Mendoza, Argentina' at the bottom of the label as a prominent piece of information. Please produce the work in size 80mm x 100mm. Feel free to use colour in addition to black/white and ensue that the label is easy to read on a shelf placement.

Target Market(s)

25-50 Year Olds who enjoy great wine that looks and appears interesting and a little different.

Requirements
Must have
• Star Logo
• Word - Malbec
• Words - Mendoza, Argentina
Nice to have
• Background image to label

```html
<!DOCTYPE html>
<html lang="en">
<head>
<meta charset="utf-8">
<title>Viento Callado — Malbec label variations</title>
<link rel="stylesheet" href="https://fonts.googleapis.com/css2?family=Old+Standard+TT:wght@400;700&family=Montserrat:wght@500;700&family=Cormorant+Garamond:wght@500&display=swap">
<style>
  :root {
    --stage: #000000;
    --mist-light: #ecebe9;
    --mist-mid: #d9dadb;
    --forest: #5d6670;
    --ink: #2a3038;
    --mark: #2c3440;
  }
  html, body {
    margin: 0;
    width: 1200px;
    height: 854px;
    overflow: hidden;
    background: var(--stage);
  }
  .sheet {
    position: relative;
    width: 1200px;
    height: 854px;
  }
  .label {
    position: absolute;
    top: 256px;
    width: 254px;
    height: 341px;
    overflow: hidden;
    color: var(--ink);
    text-align: center;
  }
  .label--bold { left: 118px; }
  .label--light { left: 473px; }
  .label--serif { left: 828px; }

  .label__scene {
    position: absolute;
    inset: 0;
    background:
      radial-gradient(ellipse 70% 14% at 40% 10%, rgba(93,102,112,0.45), transparent 70%),
      radial-gradient(ellipse 60% 22% at 10% 52%, rgba(93,102,112,0.6), transparent 70%),
      radial-gradient(ellipse 45% 12% at 60% 60%, rgba(93,102,112,0.25), transparent 70%),
      linear-gradient(180deg, var(--mist-light) 0%, var(--mist-mid) 55%, var(--mist-light) 100%);
  }

  .label__varietal {
    position: absolute;
    left: 0;
    right: 0;
    margin: 0;
  }
  .label--bold .label__varietal {
    top: 130px;
    font-family: "Montserrat", sans-serif;
    font-weight: 700;
    font-size: 11px;
    letter-spacing: 3px;
  }
  .label--bold .label__varietal span {
    display: inline-block;
    padding: 0 1px 2px 4px;
    border-top: 1px solid var(--ink);
    border-bottom: 1px solid var(--ink);
    line-height: 12px;
    padding-top: 0;
    border-top: none;
  }
  .label--light .label__varietal {
    top: 140px;
    font-family: "Montserrat", sans-serif;
    font-weight: 500;
    font-size: 10.5px;
    letter-spacing: 2.6px;
  }
  .label--serif .label__varietal {
    top: 140px;
    font-family: "Cormorant Garamond", serif;
    font-weight: 500;
    font-size: 14px;
    letter-spacing: 9px;
    padding-left: 9px;
  }

  .label__brand {
    position: absolute;
    left: 0;
    right: 0;
    top: 185px;
  }
  .label__dot {
    display: block;
    width: 24px;
    height: 24px;
    margin: 0 auto 8px;
    border-radius: 50%;
    background: var(--mark);
  }
  .label__name {
    margin: 0;
    font-family: "Old Standard TT", serif;
    font-weight: 700;
    font-size: 21px;
    line-height: 24px;
    letter-spacing: 1.5px;
    color: var(--ink);
  }

  .label__origin {
    position: absolute;
    left: 0;
    right: 0;
    top: 317px;
    margin: 0;
    font-family: "Montserrat", sans-serif;
    font-weight: 500;
    font-size: 8.5px;
    letter-spacing: 2.6px;
    padding-left: 2px;
  }
</style>
</head>
<body>
<main class="sheet">

  <article class="label label--bold">
    <div class="label__scene" role="img" aria-label="Misty mountain ridges and pine forest fading into fog"></div>
    <p class="label__varietal"><span>MALBEC</span></p>
    <div class="label__brand">
      <span class="label__dot"></span>
      <h2 class="label__name">VIENTO<br>CALLADO</h2>
    </div>
    <p class="label__origin">MENDOZA / ARGENTINA</p>
  </article>

  <article class="label label--light">
    <div class="label__scene" role="img" aria-label="Misty mountain ridges and pine forest fading into fog"></div>
    <p class="label__varietal">MALBEC</p>
    <div class="label__brand">
      <span class="label__dot"></span>
      <h2 class="label__name">VIENTO<br>CALLADO</h2>
    </div>
    <p class="label__origin">MENDOZA / ARGENTINA</p>
  </article>

  <article class="label label--serif">
    <div class="label__scene" role="img" aria-label="Misty mountain ridges and pine forest fading into fog"></div>
    <p class="label__varietal">MALBEC</p>
    <div class="label__brand">
      <span class="label__dot"></span>
      <h2 class="label__name">VIENTO<br>CALLADO</h2>
    </div>
    <p class="label__origin">MENDOZA / ARGENTINA</p>
  </article>

</main>
</body>
</html>
```